Event Planner Looking To Set Apart From Competition

I am a experienced Event/Wedding planner and need to design a unique marketing piece that will be handed out to clients and venues. I would like a postcard, but I am not opposed to another style of printed piece if it's cost effective. I am also looking for a logo that is unique to me and would like to see a few ideas.

Target Market(s)

Brides and Social Event Organizers

Industry/Entity Type

Wedding Planner

Logo Text

Mara Vintelli

Font styles to use
Script

Colors
ffffff
fee3d4
fff3d1
cfeae6
cee9f5
ecdaeb
cedeed

Requirements
Must have
• website reference _ http://www.qrdgatherings.example/planning-packages
• blog reference _ https://blogqrdgatherings.example/meet-mara/
Nice to have
• We can add text once a layout is proposed. If we like the general layout, we will send the text to be included based on the layout.

```html
<!DOCTYPE html>
<html lang="en">
<head>
<meta charset="utf-8">
<title>QRD Gatherings – Engagement Postcard</title>
<link href="https://fonts.googleapis.com/css2?family=Bebas+Neue&family=Lato:wght@400;700;900&display=swap" rel="stylesheet">
<style>
  :root{
    --page:#ecebea;
    --card:#ffffff;
    --plum:#8a1660;
    --footer:#6a1a6c;
    --ink:#1c1c1c;
    --pink-stripe:#ec8fe2;
    --blue-stripe:#86cdea;
    --glitter-a:#3d6c8c;
    --glitter-b:#9fb8d8;
    --glitter-c:#d9e2f2;
  }
  *{box-sizing:border-box;margin:0;padding:0}
  html,body{width:1200px;height:1200px;overflow:hidden;background:var(--page)}
  .postcard{position:absolute;left:0;top:200px;width:1200px;height:800px;background:var(--card);overflow:hidden;box-shadow:0 4px 14px rgba(0,0,0,.18)}
  .backdrop{position:absolute;inset:0}
  .couple-photo{position:absolute;left:0;top:0;width:1200px;height:800px}
  .brand-box{position:absolute;left:79px;top:0;width:285px;height:205px;background:#fff;box-shadow:2px 3px 6px rgba(0,0,0,.25);display:flex;flex-direction:column;align-items:center;justify-content:center;gap:14px}
  .brand-dot{width:96px;height:96px;border-radius:50%;background:#3a3a3a}
  .brand-name{font-family:'Lato',sans-serif;font-weight:400;font-size:25px;letter-spacing:1.5px;color:#3a3a3a;text-align:center;line-height:1.1}
  .headline{position:absolute;left:27px;top:250px;font-family:'Bebas Neue',sans-serif;font-weight:400;font-size:72px;line-height:1;color:var(--plum);letter-spacing:-.5px}
  .subhead{position:absolute;left:27px;top:322px;font-family:'Lato',sans-serif;font-weight:900;color:var(--ink);line-height:1.25}
  .subhead .line-one{display:block;font-size:41px}
  .subhead .line-two{display:block;font-size:34px;margin-top:2px}
  .intro{position:absolute;left:27px;top:446px;width:620px;font-family:'Lato',sans-serif;font-size:14.5px;line-height:19px;color:var(--ink)}
  .gallery{position:absolute;left:27px;top:599px;display:flex;gap:24px}
  .gallery-photo{width:190px;height:118px;border-radius:10px;border:3px solid #fff;box-shadow:0 0 0 1.5px #7a4a3a}
  .gallery-photo.first{background:linear-gradient(135deg,#8a5fc8,#3a2a6a 60%,#d7c8ee)}
  .gallery-photo.second{background:linear-gradient(135deg,#5b3a1a,#2a1c10 55%,#e9e4e0)}
  .gallery-photo.third{background:linear-gradient(135deg,#b9b0a6,#4a3324 55%,#f1eeea)}
  .contact-bar{position:absolute;left:0;top:736px;width:830px;height:64px;background:var(--footer);display:flex;align-items:center;padding-left:27px;gap:18px;font-family:'Lato',sans-serif;font-size:17px;color:#fff;white-space:nowrap}
  .contact-item{display:flex;align-items:center;gap:7px}
  .contact-item svg{width:22px;height:22px;flex:none}
  .social-links{display:flex;gap:16px;margin-left:6px}
  .social-circle{width:43px;height:43px;border-radius:50%;border:2.5px solid #fff}
</style>
</head>
<body>
<main class="postcard">
  <svg class="backdrop" viewBox="0 0 1200 800" width="1200" height="800">
    <defs>
      <linearGradient id="glitterTone" x1="0" y1="0" x2="1" y2="1">
        <stop offset="0" stop-color="var(--glitter-a)"/>
        <stop offset=".45" stop-color="var(--glitter-b)"/>
        <stop offset=".75" stop-color="var(--glitter-c)"/>
        <stop offset="1" stop-color="var(--glitter-a)"/>
      </linearGradient>
    </defs>
    <polygon role="img" aria-label="Sparkling blue glitter background" points="0,0 1200,0 1200,376 0,164" fill="url(#glitterTone)"/>
    <polygon points="0,164 1200,376 1200,383 0,171" fill="var(--pink-stripe)"/>
    <polygon points="0,171 1200,383 1200,391 0,179" fill="var(--blue-stripe)"/>
  </svg>

  <svg class="couple-photo" viewBox="0 0 1200 800" width="1200" height="800">
    <defs>
      <linearGradient id="coupleTone" x1="0" y1="0" x2="1" y2="0">
        <stop offset="0" stop-color="#f4f4f6"/>
        <stop offset=".5" stop-color="#e8e6e8"/>
        <stop offset=".72" stop-color="#2b3552"/>
        <stop offset="1" stop-color="#1d253d"/>
      </linearGradient>
    </defs>
    <path role="img" aria-label="Bride in white veil and fur wrap embracing groom in navy suit, holding a white and blue bouquet"
          d="M790,800 L720,640 C680,520 720,300 800,150 C860,75 960,55 1050,72 C1120,86 1185,120 1200,140 L1200,800 Z"
          fill="url(#coupleTone)"/>
  </svg>

  <div class="brand-box">
    <div class="brand-dot"></div>
    <div class="brand-name">QRD GATHERINGS</div>
  </div>

  <h1 class="headline">CONGRATULATIONS!</h1>
  <h2 class="subhead">
    <span class="line-one">You’re engaged, and it’s time</span>
    <span class="line-two">for the wedding planning to begin</span>
  </h2>

  <p class="intro">If you’re engaged and don’t know where to begin, this is the package for you!&nbsp; We’ll start with a vision meeting to understand your style and determine your budget. From there, we’ll guide you through the entire planning process, offering creative solutions and valuable advice at every turn. We’ll create your wedding timeline, and you’ll have our help with every wedding detail, from selecting the ceremony content to handling a guest's gluten free request. On wedding day, we’ll orchestrate all those perfectly planned elements into a symphony of beautiful moments while you relax and enjoy your celebration.</p>

  <div class="gallery">
    <div class="gallery-photo first" role="img" aria-label="Couple's first dance surrounded by guests under purple lighting"></div>
    <div class="gallery-photo second" role="img" aria-label="Flower girls in white dresses at the reception"></div>
    <div class="gallery-photo third" role="img" aria-label="Bride dancing in a ballroom with a monogram projected on the floor"></div>
  </div>

  <footer class="contact-bar">
    <span class="contact-item">
      <svg viewBox="0 0 24 24" aria-hidden="true"><path d="M6.5 3.5l3 3-2 2.5c1.2 2.6 3.4 4.8 6 6l2.5-2 3 3-2.2 2.5C11 18 6 13 4 5.7z" fill="none" stroke="#fff" stroke-width="1.8" stroke-linejoin="round"/></svg>
      555.014.2271
    </span>
    <span class="contact-item">
      <svg viewBox="0 0 24 24" aria-hidden="true"><rect x="7" y="3" width="10" height="6" fill="none" stroke="#fff" stroke-width="1.8"/><rect x="3" y="9" width="18" height="8" rx="1.5" fill="#fff"/><rect x="7" y="14" width="10" height="7" fill="#fff" stroke="var(--footer)" stroke-width="1.2"/></svg>
      555.019.3384
    </span>
    <span class="contact-item">
      <svg viewBox="0 0 24 24" aria-hidden="true"><circle cx="12" cy="12" r="8" fill="none" stroke="#fff" stroke-width="1.8"/><ellipse cx="12" cy="12" rx="3.5" ry="8" fill="none" stroke="#fff" stroke-width="1.4"/><line x1="4" y1="12" x2="20" y2="12" stroke="#fff" stroke-width="1.4"/></svg>
      www.qrdgatherings.example
    </span>
    <span class="social-links">
      <span class="social-circle"></span>
      <span class="social-circle"></span>
      <span class="social-circle"></span>
    </span>
  </footer>
</main>
</body>
</html>
```